Portugal:the best eco sun-dried tomato in the world needs a packaging design

We produce the best sun-dried tomatoes in the world...we know that, even that competition doesn´t exist...yet!
We are a "solar farm" in Portugal, reducing carbon footprint producing beautiful and healthy local food, with mules...the traditional way in a new way. Our tomatoes are hand-picked and sun dried, in a very "slow food" way.
The costumers for our product -we are a small farm - can only be good foodstores and airports, we'd love to export the best of Portugal elsewhere. In a glass jar of c. 250 ml, with a nice top and a nice logo+description...one that stands out of the others and conveys our eco, local, solar message.
Oh, and I forgot...our sun-dried tomatoes are packed with our beautiful olive oil..and yes, that olive oil has already won the best olive oil in the world! For sure!
I'll send photos for the interested, you'll love it; and the best olive oil and sun-dried tomatoes in the world for the winner!

Target Market(s)

nice foodstores
foodies
airport stores

Industry/Entity Type

Food Store

Font styles to use
Decorative
Script

Requirements
Must have
• Portugal
• Sun dried tomatoes
• Best olive oil in the world
• Traditional methods
• Sustainable farming
Nice to have
• a photo of our mules working...sent to interested designers

```html
<!DOCTYPE html>
<html lang="en">
<head>
<meta charset="utf-8">
<title>Sun Dried Tomatoes in Olive Oil — Label</title>
<link rel="stylesheet" href="https://fonts.googleapis.com/css2?family=Great+Vibes&family=Playfair+Display:wght@400;700&display=swap">
<style>
  :root {
    --canvas-bg: #ffffff;
    --label-paper: #f6f0f1;
    --label-edge: #e6dcde;
    --ink: #2f3034;
    --ink-soft: #55565b;
    --pill-bg: #2e2f33;
    --pill-text: #f4f1f1;
    --scene-light: #e9e4e4;
    --scene-mid: #c9c3c4;
  }
  * { margin: 0; padding: 0; box-sizing: border-box; }
  html, body {
    width: 1200px;
    height: 1200px;
    overflow: hidden;
    background: var(--canvas-bg);
  }
  .canvas {
    position: relative;
    width: 1200px;
    height: 1200px;
  }
  .label {
    position: absolute;
    left: 100px;
    top: 171px;
    width: 1000px;
    height: 858px;
    background: var(--label-paper);
    border: 1px solid var(--label-edge);
    color: var(--ink);
    text-align: center;
  }
  .farm-scene {
    position: absolute;
    left: 152px;
    top: 65px;
    width: 674px;
    height: 217px;
  }
  .tagline-script {
    position: absolute;
    left: 0;
    right: 0;
    top: 272px;
    font-family: "Great Vibes", cursive;
    font-size: 96px;
    line-height: 110px;
    color: var(--ink);
  }
  .product-name {
    position: absolute;
    left: 0;
    right: 0;
    top: 372px;
    font-family: "Playfair Display", serif;
    font-weight: 400;
    font-size: 150px;
    line-height: 122px;
    letter-spacing: -4px;
    text-transform: uppercase;
    color: var(--ink);
  }
  .product-name span { display: block; }
  .packing-script {
    position: absolute;
    left: 0;
    right: 0;
    top: 652px;
    font-family: "Great Vibes", cursive;
    font-size: 82px;
    line-height: 100px;
    color: var(--ink);
  }
  .eco-pill {
    position: absolute;
    left: 245px;
    top: 749px;
    width: 500px;
    height: 40px;
    border-radius: 20px;
    background: var(--pill-bg);
    color: var(--pill-text);
    font-family: "Playfair Display", serif;
    font-weight: 700;
    font-size: 21px;
    letter-spacing: 2px;
    line-height: 40px;
    text-transform: uppercase;
  }
</style>
</head>
<body>
  <main class="canvas">
    <section class="label">
      <svg class="farm-scene" role="img" aria-label="Engraved-style illustration of rolling Portuguese farmland with a farmhouse, cypress trees, ploughed fields and hay bales" viewBox="0 0 674 217" preserveAspectRatio="none">
        <defs>
          <linearGradient id="sceneTone" x1="0" y1="0" x2="0" y2="1">
            <stop offset="0" stop-color="var(--label-paper)"/>
            <stop offset="0.35" stop-color="var(--scene-light)"/>
            <stop offset="1" stop-color="var(--scene-mid)"/>
          </linearGradient>
        </defs>
        <rect x="0" y="0" width="674" height="217" fill="url(#sceneTone)"/>
      </svg>

      <p class="tagline-script">Portugal’s Best</p>
      <h1 class="product-name"><span>Sun Dried</span><span>Tomatoes</span></h1>
      <p class="packing-script">in Olive Oil</p>
      <p class="eco-pill">Sustainable Farming Product</p>
    </section>
  </main>
</body>
</html>
```